Zielgruppe
Strandhaus mit Restaurant (Beach feeling)
Zielgruppe: gehoben, edel, teuer
Aufgabenstellung
Auf stilsicherheit und das es stylisch und gleichzeitig edel aussieht.
Format:
Breite 44,5
Höher 71
Text:
Logo oben gut sichtbar
Herzlich Willkommen! (andere Schriftart)
MONTAG - FREITAG
SAMSTAG - SONNTAG
Unsere Küche verwöhnt dich bis 21:00 Uhr - täglich frisch & mit Liebe gekocht.
Wolkenhain ist mehr als ein Ort - es ist ein Gefühl. (andere Schriftart)
Lindenmoor, Kastner Weg 58-60, 2700 Wiener Neustadt
www.wolkenhain-beispiel.at/reservieren

```html
<!DOCTYPE html>
<html lang="de">
<head>
<meta charset="utf-8">
<title>Wolkenhain – Willkommen</title>
<link href="https://fonts.googleapis.com/css2?family=Allura&family=Dancing+Script:wght@600;700&family=Poppins:wght@400;600&display=swap" rel="stylesheet">
<style>
  :root {
    --page: #fbf4ee;
    --brown: #6b3f27;
    --ink: #1a1410;
    --arch: rgba(241, 239, 235, 0.9);
    --white: #ffffff;
  }
  html, body { margin: 0; padding: 0; overflow: hidden; }
  body { width: 1200px; height: 1200px; background: var(--page); position: relative; }
  .poster {
    position: absolute; left: 223px; top: 0; width: 753px; height: 1200px; overflow: hidden;
  }
  .backdrop {
    position: absolute; inset: 0;
    background:
      linear-gradient(90deg, rgba(70,48,30,0.55) 0%, rgba(70,48,30,0) 35%),
      linear-gradient(180deg, #6b5443 0%, #8a7565 35%, #7e7468 62%, #4f5a52 78%, #5c6a62 100%);
  }
  .brand {
    position: absolute; left: 0; right: 0; top: 88px; text-align: center;
    font-family: "Poppins", sans-serif; font-weight: 400; font-size: 38px;
    color: var(--white); letter-spacing: 1px;
  }
  .arch {
    position: absolute; left: 65px; top: 196px; width: 623px; height: 1004px;
    background: var(--arch); border-radius: 311.5px 311.5px 6px 6px;
  }
  .c { position: absolute; text-align: center; white-space: nowrap; transform: translateX(-50%); margin: 0; }
  .welcome {
    font-family: "Dancing Script", "Allura", cursive; font-weight: 700;
    color: var(--brown); font-size: 86px; line-height: 1;
  }
  .days {
    font-family: "Dancing Script", "Allura", cursive; font-weight: 600;
    color: var(--brown); font-size: 22px; line-height: 1; text-transform: uppercase;
  }
  .time { font-family: "Poppins", sans-serif; color: var(--ink); font-size: 22px; line-height: 1; }
  .kitchen {
    font-family: "Poppins", sans-serif; font-weight: 600; color: var(--brown);
    font-size: 22px; line-height: 29px;
  }
  .until {
    font-family: "Dancing Script", "Allura", cursive; font-weight: 600;
    color: var(--brown); font-size: 54px; line-height: 1;
  }
  .note { font-family: "Allura", cursive; color: var(--ink); font-size: 36px; line-height: 1; }
  .claim {
    font-family: "Poppins", sans-serif; font-weight: 600; color: var(--brown);
    font-size: 28px; line-height: 36px;
  }
  .contact { font-family: "Poppins", sans-serif; color: var(--ink); font-size: 16.5px; line-height: 1; }
  .divider { position: absolute; width: 3px; background: var(--ink); }
  .rule { position: absolute; height: 2px; background: var(--brown); }
</style>
</head>
<body>
  <div class="poster">
    <div class="backdrop" role="img" aria-label="Gedämpftes Strandfoto mit Palme, Meer und bewaldeter Küste"></div>
    <div class="brand">Wolkenhain</div>
    <div class="arch"></div>

    <p class="c welcome" style="left:377px; top:318px;">Herzlich</p>
    <p class="c welcome" style="left:377px; top:420px;">Willkommen!</p>

    <p class="c days" style="left:200px; top:598px;">Montag - Freitag</p>
    <p class="c time" style="left:227px; top:640px;">11:00 - 00:00</p>
    <div class="divider" style="left:376px; top:605px; height:66px;"></div>
    <p class="c days" style="left:510px; top:598px;">Samstag - Sonntag</p>
    <p class="c time" style="left:531px; top:640px;">09:00 - 00:00</p>

    <p class="c kitchen" style="left:227px; top:738px;">Unsere Küche<br>verwöhnt dich bis</p>
    <div class="divider" style="left:376px; top:740px; height:68px;"></div>
    <p class="c until" style="left:523px; top:742px;">21:00 Uhr</p>

    <p class="c note" style="left:368px; top:840px;">täglich frisch &amp; mit Liebe gekocht.</p>
    <div class="rule" style="left:314px; top:906px; width:126px;"></div>

    <p class="c claim" style="left:377px; top:922px;">Wolkenhain ist mehr<br>als ein Ort</p>
    <p class="c note" style="left:377px; top:1008px;">es ist ein Gefühl.</p>
    <div class="rule" style="left:314px; top:1085px; width:126px;"></div>

    <p class="c contact" style="left:377px; top:1105px;">Lindenmoor, Kastner Weg 58-60, 2700 Wiener Neustadt</p>
    <p class="c contact" style="left:377px; top:1137px;">www.wolkenhain-beispiel.at/reservieren</p>
  </div>
</body>
</html>
```